Vantrel Card

We want a business card that shows people who we are the log attached was designed by the designers on craft hive,we are using the OO in the logo (speech bubbles as our icon,so please make that part of the card ) keep the colouring the same as the logo design and we will be using high end production on the card using silver foil as the icon to make it stand out.
As Vantrel we specialise in finding influencers through social networks for brands, so if you used flimbo to comment about sports products and you were followed by of lot of users and interacted with those users then the algorithm finds you and we contact you to work for our clients as a company we then have a set of influencers that we use to support new sports products.
Also we use our algorithm to help athletes,models etc to be scored via there digital influence so when say Vorta KX ask me to find a skater that is not so much a podium rider but is more digital focused for a digital campaign then we work out who those guys or girls are to help Vorta KX
Vantrel is the name of the product and company, However I just wanted to give you the rationale of why we chose vantrel in the first place. Marbo itself is an 'abbreviation' from the proper name Alsander Wick from Tale of the Iron Hills. The character was able to look into the eskavor (sometimes translated as "Seeing Stone" but literally meaning "Farsighted" or "One that Sees from Afar") and see into the far corners of the Universe. Much in the same way as the platform has been developed is able to look into the far corners of the social network arena to help brands and Athletes will be able to see how they rated....but don't worry i don't go running around in the woods with a foam Axe and an army of dwarfs!!!
Digital Directors,Brand Directors,Athletes,Models,Celebrities and agents
Business

```html
<!DOCTYPE html>
<html lang="en">
<head>
<meta charset="utf-8">
<title>Vantrel Business Card</title>
<link rel="stylesheet" href="https://fonts.googleapis.com/css2?family=Open+Sans:wght@400;600;700&display=swap">
<style>
  :root {
    --brand-blue: #48bdec;
    --brand-blue-deep: #41a8d3;
    --brand-blue-shade: #3fa6d2;
    --brand-grey: #808285;
    --paper: #ffffff;
    --canvas: #ffffff;
    --card-radius: 16px;
  }
  html, body {
    margin: 0;
    padding: 0;
    width: 1200px;
    height: 900px;
    overflow: hidden;
    background: var(--canvas);
    font-family: "Open Sans", Arial, sans-serif;
  }
  .stage {
    position: relative;
    width: 1200px;
    height: 900px;
  }
  .card {
    position: absolute;
    width: 520px;
    height: 320px;
    border-radius: var(--card-radius);
    overflow: hidden;
    box-shadow: 0 0 0 1px rgba(0,0,0,0.08);
  }

  .wordmark {
    margin: 0;
    font-weight: 700;
    letter-spacing: -1px;
    line-height: 1;
  }
  .brand-lockup {
    display: flex;
    align-items: center;
    gap: 14px;
  }
  .brand-dot {
    flex: none;
    border-radius: 50%;
    background: var(--brand-grey);
  }

  /* Front of card */
  .card--front {
    left: 560px;
    top: 110px;
    background: var(--brand-blue);
  }
  .front__header {
    height: 140px;
    background: var(--paper);
    display: flex;
    align-items: center;
    padding-left: 44px;
  }
  .front__header .wordmark {
    font-size: 84px;
    color: var(--brand-blue);
  }
  .front__header .brand-dot {
    width: 46px;
    height: 46px;
    margin-top: 18px;
  }
  .front__band {
    height: 22px;
    background: var(--brand-grey);
  }
  .front__body {
    position: relative;
    height: 158px;
  }
  .front__details {
    position: relative;
    padding: 30px 0 0 40px;
    color: var(--paper);
  }
  .icon-watermark {
    position: absolute;
    right: 26px;
    top: 14px;
    width: 200px;
    height: 130px;
    border-radius: 65px;
    background: radial-gradient(ellipse at center, var(--brand-blue-shade) 0%, var(--brand-blue-shade) 55%, rgba(63,166,210,0) 100%);
  }
  .person-name {
    margin: 0;
    font-size: 17px;
    font-weight: 700;
    color: var(--brand-grey);
    letter-spacing: 0.3px;
  }
  .person-role {
    margin: 0 0 12px;
    font-size: 13px;
    font-weight: 400;
  }
  .contact-list {
    list-style: none;
    margin: 0;
    padding: 0;
    font-size: 14px;
    line-height: 21px;
  }
  .contact-list li {
    display: flex;
    align-items: center;
    gap: 8px;
  }
  .contact-icon {
    width: 12px;
    height: 12px;
    flex: none;
  }

  /* Back of card */
  .card--back {
    left: 120px;
    top: 470px;
    background: var(--brand-blue-deep);
  }
  .back__curves {
    position: absolute;
    left: 0;
    top: 0;
    width: 190px;
    height: 320px;
    background: linear-gradient(90deg, var(--brand-blue) 0%, var(--brand-blue-deep) 40%, var(--brand-blue) 70%, var(--brand-blue-deep) 100%);
  }
  .back__disc {
    position: absolute;
    left: 190px;
    top: -10px;
    width: 290px;
    height: 290px;
    border-radius: 50%;
    background: var(--brand-blue);
  }
  .back__logo {
    position: absolute;
    left: 210px;
    top: 100px;
    width: 250px;
    justify-content: center;
  }
  .back__logo .wordmark {
    font-size: 58px;
    color: var(--paper);
  }
  .back__logo .brand-dot {
    width: 32px;
    height: 32px;
    margin-top: 12px;
  }
</style>
</head>
<body>
<main class="stage">

  <section class="card card--front" aria-label="Business card front">
    <header class="front__header">
      <div class="brand-lockup">
        <h1 class="wordmark">vantrel</h1>
        <span class="brand-dot" aria-hidden="true"></span>
      </div>
    </header>
    <div class="front__band"></div>
    <div class="front__body">
      <div class="icon-watermark" role="img" aria-label="Large faint speech-bubble brand icon in silver foil"></div>
      <div class="front__details">
        <p class="person-name">OWEN HARTLEY</p>
        <p class="person-role">Director</p>
        <ul class="contact-list">
          <li>
            <svg class="contact-icon" viewBox="0 0 12 12" aria-hidden="true">
              <rect x="0.5" y="0.5" width="11" height="11" rx="2" fill="var(--brand-grey)"/>
              <rect x="3.5" y="2" width="5" height="8" rx="1" fill="none" stroke="#fff" stroke-width="1"/>
            </svg>
            07 700 900412
          </li>
          <li>
            <svg class="contact-icon" viewBox="0 0 12 12" aria-hidden="true">
              <rect x="0.5" y="0.5" width="11" height="11" rx="2" fill="var(--brand-grey)"/>
              <rect x="2.5" y="3.5" width="7" height="5" fill="none" stroke="#fff" stroke-width="1"/>
              <path d="M2.5 3.5 L6 6.5 L9.5 3.5" fill="none" stroke="#fff" stroke-width="1"/>
            </svg>
            owenhartley@Vantrel.com
          </li>
          <li>
            <svg class="contact-icon" viewBox="0 0 12 12" aria-hidden="true">
              <rect x="0.5" y="0.5" width="11" height="11" rx="2" fill="var(--brand-grey)"/>
              <circle cx="6" cy="6" r="3.5" fill="none" stroke="#fff" stroke-width="1"/>
              <path d="M2.5 6 H9.5 M6 2.5 V9.5" stroke="#fff" stroke-width="0.8"/>
            </svg>
            www.vantrel.com.uk
          </li>
        </ul>
      </div>
    </div>
  </section>

  <section class="card card--back" aria-label="Business card back">
    <div class="back__curves" role="img" aria-label="Large cropped speech-bubble brand icon curves in light and deep blue"></div>
    <div class="back__disc"></div>
    <div class="brand-lockup back__logo">
      <p class="wordmark">vantrel</p>
      <span class="brand-dot" aria-hidden="true"></span>
    </div>
  </section>

</main>
</body>
</html>
```